Marlow Crate Works Business Cards

WHAT WE DOWe RepairWe CustomizeWe ManufactureWe Deliver
Reason: Hello,
I would like to extend the deadline to May 1st - no additional fee. Reason being is because I am waiting on a reply from feedback from the designed that we are planning on choosing. I would like an answer as soon as possible, please and thanks!!!
Industry/Entity Type
Business
Contact Information for Business Card
Denise Okafor
Vice President
Office: 555-210-4471
Cell: 555-386-9124
Fax: 555-210-4472
denise@marlowcrate.example
Marlow Crate Works II, Inc
2630 Thornbury Road
Fallowmere, IL 60999
www.marlowcrate.example
Look and feel
Each slider illustrates characteristics of the customer's brand and the style your logo design should communicate.

```html
<!DOCTYPE html>
<html lang="en">
<head>
<meta charset="utf-8">
<title>Marlow Crate Works – Business Cards</title>
<link rel="stylesheet" href="https://fonts.googleapis.com/css2?family=Graduate&family=Courier+Prime:ital@0;1&family=Share+Tech+Mono&display=swap">
<style>
  :root {
    --page-bg: #eceef0;
    --card-dark: #2a2a2a;
    --card-dark-soft: #353535;
    --card-light: #ffffff;
    --ink-light: #f2f2f2;
    --ink-muted: #bdbdbd;
    --ink-dark: #1c1c1c;
    --ink-body: #3a3a3a;
    --shadow: rgba(0, 0, 0, 0.28);
  }
  * { box-sizing: border-box; margin: 0; padding: 0; }
  html, body {
    width: 1200px;
    height: 1059px;
    overflow: hidden;
    background: var(--page-bg);
  }
  .sheet {
    width: 1200px;
    height: 1059px;
    display: flex;
    align-items: center;
    justify-content: center;
    gap: 56px;
  }
  .card {
    position: relative;
    width: 540px;
    height: 308px;
    box-shadow: 4px 6px 10px var(--shadow);
    overflow: hidden;
  }

  /* Front */
  .card-front {
    background: var(--card-dark);
    color: var(--ink-light);
  }
  .card-front .texture {
    position: absolute;
    inset: 0;
    background: linear-gradient(135deg, var(--card-dark-soft), var(--card-dark) 60%);
  }
  .company-name {
    position: absolute;
    top: 92px;
    left: 0;
    right: 0;
    text-align: center;
    font-family: "Graduate", serif;
    font-size: 33px;
    line-height: 1.2;
    letter-spacing: 2px;
    color: var(--ink-light);
  }
  .services {
    position: absolute;
    bottom: 18px;
    left: 0;
    right: 0;
    text-align: center;
    font-family: "Share Tech Mono", monospace;
    font-size: 15px;
    letter-spacing: 1.6px;
    color: var(--ink-muted);
  }

  /* Back */
  .card-back {
    background: var(--card-light);
    color: var(--ink-body);
  }
  .person-name {
    position: absolute;
    top: 54px;
    left: 0;
    right: 0;
    text-align: center;
    font-family: "Graduate", serif;
    font-size: 21px;
    letter-spacing: 1.2px;
    color: var(--ink-dark);
  }
  .person-title {
    position: absolute;
    top: 84px;
    left: 0;
    right: 0;
    text-align: center;
    font-family: "Courier Prime", monospace;
    font-style: italic;
    font-size: 14px;
    letter-spacing: 0.8px;
  }
  .address, .contacts {
    position: absolute;
    left: 18px;
    font-family: "Courier Prime", monospace;
    font-size: 13px;
    line-height: 16px;
    letter-spacing: 0.4px;
  }
  .address { top: 150px; }
  .contacts { top: 210px; }
  .contacts dt {
    float: left;
    clear: left;
    width: 58px;
    color: var(--ink-dark);
    font-weight: 700;
  }
  .contacts dd { margin-left: 58px; }
</style>
</head>
<body>
  <main class="sheet">
    <section class="card card-front" aria-label="Business card front">
      <div class="texture" role="img" aria-label="Dark pattern of outlined wooden pallets"></div>
      <h1 class="company-name">MARLOW CRATE WORKS<br>INC</h1>
      <p class="services">REPAIR - CUSTOMIZE - MANUFACTURE - DELIVER</p>
    </section>

    <section class="card card-back" aria-label="Business card back">
      <h2 class="person-name">DENISE OKAFOR</h2>
      <p class="person-title">Vice President</p>
      <address class="address">
        2630 Thornbury Road<br>
        Fallowmere, IL 60999
      </address>
      <dl class="contacts">
        <dt>Office</dt><dd>555-210-4471</dd>
        <dt>Cell</dt><dd>555-386-9124</dd>
        <dt>Fax</dt><dd>555-210-4472</dd>
      </dl>
    </section>
  </main>
</body>
</html>
```